11 x 11 Flyer Design for Social Media - Reverse Mortgages

62 or older?

A Reverse Mortgage
could be
Your Road to Financial Freedom

* No Monthly Payments
* No Income Requirements
* No Credit Score Requirements
* No Loss of Ownership

Receive cash by lump sum, monthly installments or a line of credit!!

Call us today for a Free Consultation!!
(800) 471-2965

Bluegate Financial Services, Inc.
NMLS #318760
www.bluegatehome.com

```html
<!DOCTYPE html>
<html lang="en">
<head>
<meta charset="utf-8">
<title>Reverse Mortgage Flyer – Bluegate Financial Services</title>
<link href="https://fonts.googleapis.com/css2?family=Roboto+Condensed:wght@300;700&family=Roboto:wght@400;700&display=swap" rel="stylesheet">
<style>
  :root {
    --page-bg: #e4e4e4;
    --brand-blue: #1261a8;
    --band-grey: #a9acb0;
    --gold: #a99a3c;
    --khaki: #d5cd9c;
    --cream: #f2efdf;
    --ink: #2a2a2a;
    --headline: #3d3d3d;
    --photo-warm: #b58a66;
    --photo-sky: #9fb7c9;
    --white: #ffffff;
  }
  * { box-sizing: border-box; margin: 0; padding: 0; }
  html, body { width: 892px; height: 1200px; overflow: hidden; }
  body { background: var(--page-bg); position: relative; font-family: "Roboto", sans-serif; }

  .flyer {
    position: absolute; left: 20px; top: 174px;
    width: 852px; height: 852px; overflow: hidden;
    background: linear-gradient(180deg, var(--white) 0%, var(--white) 36%, var(--cream) 50%, var(--khaki) 80%, var(--khaki) 100%);
    box-shadow: 0 10px 30px rgba(0,0,0,.18);
  }
  .flyer__art { position: absolute; inset: 0; }

  .brand {
    position: absolute; left: 26px; top: 62px;
    display: flex; align-items: center; gap: 10px;
    font-family: "Roboto Condensed", sans-serif; font-weight: 700;
    font-size: 19px; color: var(--brand-blue);
  }
  .brand__dot { width: 30px; height: 30px; border-radius: 50%; background: var(--brand-blue); }

  .headline {
    position: absolute; left: 28px; top: 134px;
    font-family: "Roboto Condensed", sans-serif; font-weight: 700;
    font-size: 64px; line-height: 1; color: var(--headline);
    text-shadow: 2px 2px 0 var(--white);
  }

  .tagline {
    position: absolute; left: 22px; top: 202px;
    font-family: "Roboto Condensed", sans-serif; font-size: 33px;
    line-height: 44px; color: var(--white); font-weight: 300;
  }
  .tagline strong { font-weight: 700; }

  .benefits { position: absolute; left: 64px; top: 325px; list-style: none; }
  .benefits li {
    display: flex; align-items: center; gap: 18px;
    height: 53px; font-size: 25px; color: var(--ink);
  }
  .benefits svg { width: 24px; height: 24px; }

  .payout {
    position: absolute; left: 45px; top: 542px;
    font-size: 25px; line-height: 29px; color: var(--ink);
  }

  .contact {
    position: absolute; left: 40px; top: 660px; width: 410px;
    text-align: center; color: var(--ink);
  }
  .contact__call { font-weight: 700; font-size: 33px; letter-spacing: 2px; color: var(--brand-blue); line-height: 34px; }
  .contact__offer { font-size: 33px; letter-spacing: 1px; line-height: 34px; }
  .contact__phone { font-weight: 700; font-size: 34px; letter-spacing: 1px; line-height: 34px; }
  .contact__web { font-size: 20px; color: var(--brand-blue); line-height: 26px; }
  .contact__license { font-size: 16px; color: var(--ink); line-height: 22px; }
</style>
</head>
<body>
  <main class="flyer">
    <svg class="flyer__art" width="852" height="852" viewBox="0 0 852 852">
      <rect x="0" y="166" width="620" height="146" fill="var(--band-grey)"/>
      <rect x="0" y="172" width="620" height="134" fill="var(--brand-blue)"/>
      <path d="M852 322 C760 352 640 340 598 300 C575 200 640 40 830 0 L852 0 Z" fill="var(--brand-blue)"/>
      <path d="M852 312 C760 342 648 330 606 292 C590 200 650 40 830 0 L852 0 Z" fill="var(--photo-warm)" role="img" aria-label="Photo of an older woman reading her phone at home"/>
      <path d="M600 170 C640 70 720 20 830 0" fill="none" stroke="var(--gold)" stroke-width="4"/>
      <circle cx="685" cy="393" r="88" fill="var(--gold)"/>
      <circle cx="685" cy="393" r="82" fill="#8f7a6a" role="img" aria-label="Photo of a laughing senior couple"/>
      <circle cx="683" cy="520" r="80" fill="var(--gold)"/>
      <circle cx="683" cy="520" r="74" fill="#9b9c8c" role="img" aria-label="Photo of a smiling senior couple outdoors"/>
      <circle cx="685" cy="650" r="66" fill="var(--gold)"/>
      <circle cx="685" cy="650" r="60" fill="var(--photo-sky)" role="img" aria-label="Photo of a senior couple at the beach"/>
    </svg>

    <div class="brand"><span class="brand__dot"></span>Bluegate Financial Services, Inc.</div>

    <h1 class="headline">62 or older?</h1>

    <p class="tagline">
      <strong>A REVERSE MORTGAGE</strong> COULD BE<br>
      <strong>YOUR ROAD</strong> TO <strong>FINANCIAL FREEDOM</strong>
    </p>

    <ul class="benefits">
      <li><svg viewBox="0 0 24 24"><circle cx="12" cy="12" r="11" fill="#a99a3c"/><path d="M6.5 12.5l3.5 3.5 7-7.5" fill="none" stroke="#fff" stroke-width="2.6"/></svg>No Monthly Payments</li>
      <li><svg viewBox="0 0 24 24"><circle cx="12" cy="12" r="11" fill="#a99a3c"/><path d="M6.5 12.5l3.5 3.5 7-7.5" fill="none" stroke="#fff" stroke-width="2.6"/></svg>No Income Requirements</li>
      <li><svg viewBox="0 0 24 24"><circle cx="12" cy="12" r="11" fill="#a99a3c"/><path d="M6.5 12.5l3.5 3.5 7-7.5" fill="none" stroke="#fff" stroke-width="2.6"/></svg>No Credit Score Requirements</li>
      <li><svg viewBox="0 0 24 24"><circle cx="12" cy="12" r="11" fill="#a99a3c"/><path d="M6.5 12.5l3.5 3.5 7-7.5" fill="none" stroke="#fff" stroke-width="2.6"/></svg>No Loss of Ownership</li>
    </ul>

    <p class="payout">Receive cash by lump sum,<br>monthly installments or a line of credit!!</p>

    <section class="contact">
      <p class="contact__call">CALL US TODAY</p>
      <p class="contact__offer">for a Free Consultation!!</p>
      <p class="contact__phone">(800) 471-2965</p>
      <p class="contact__web">www.bluegatehome.com</p>
      <p class="contact__license">NMLS #318760</p>
    </section>
  </main>
</body>
</html>
```